Harbinger Crude Advisors needs a logo design and business card layout.

HCA is a consulting firm in oil and gas, specializing in upstream engineering and field work. We provide engineering solutions for the complete wellbore cycle from casing design to flowback. This includes completion and production design. On-site job supervision and project engineering for conventional and unconventional reservoirs. Asset analysis by reviewing operational conditions of asset packages to determine value of potential acquisitions or divesture.

```html
<!DOCTYPE html>
<html lang="en">
<head>
<meta charset="utf-8">
<title>Harbinger Crude Advisors — Business Card</title>
<link href="https://fonts.googleapis.com/css2?family=Michroma&family=Montserrat:wght@700;800&family=Arimo:wght@400&display=swap" rel="stylesheet">
<style>
  :root {
    --backdrop: #1c1c1c;
    --card: #0d0d0d;
    --card-edge: #161616;
    --orange: #f07a1a;
    --amber: #f9b21c;
    --red: #e0301e;
    --white: #ffffff;
    --silver: #bdbdbd;
    --steel: #6a6a6a;
    --muted: #d8d8d8;
  }
  * { margin: 0; padding: 0; box-sizing: border-box; }
  html, body { width: 1200px; height: 1200px; overflow: hidden; background: var(--backdrop); }
  .stage {
    width: 1200px; height: 1200px;
    display: flex; flex-direction: column; align-items: center; justify-content: center; gap: 40px;
  }
  .card {
    position: relative;
    width: 900px; height: 514px;
    border-radius: 22px;
    background: linear-gradient(160deg, var(--card-edge), var(--card) 60%);
    box-shadow: 0 18px 40px rgba(0,0,0,.55);
    overflow: hidden;
  }
  /* back side */
  .card-back .wordmark {
    position: absolute; left: 0; right: 0; top: 190px;
    display: flex; align-items: center; justify-content: center; gap: 28px;
  }
  .card-back .mark-dot {
    width: 64px; height: 64px; border-radius: 50%;
    background: #2a2a2a;
  }
  .card-back .company {
    font-family: "Michroma", sans-serif;
    font-size: 34px; letter-spacing: 2px; line-height: 1.25;
    color: var(--steel);
  }
  .card-back .company span { display: block; font-size: 18px; letter-spacing: 6px; }
  .card-back .tagline {
    position: absolute; left: 0; right: 0; bottom: 46px; text-align: center;
    font-family: "Arimo", sans-serif; font-size: 16px; color: var(--muted);
  }
  /* front side */
  .card-front .company {
    position: absolute; left: 60px; top: 60px;
    font-family: "Michroma", sans-serif;
    font-size: 40px; letter-spacing: 2px; line-height: 1.2;
    color: var(--orange);
  }
  .card-front .company span { display: block; font-size: 20px; letter-spacing: 6px; }
  .person { position: absolute; left: 60px; top: 210px; font-family: "Montserrat", sans-serif; }
  .person .name { font-size: 26px; font-weight: 800; letter-spacing: 2px; color: var(--white); }
  .person .role { font-size: 19px; font-weight: 700; letter-spacing: 1px; color: var(--red); margin-top: 2px; }
  .contact {
    position: absolute; left: 60px; top: 300px;
    font-family: "Arimo", sans-serif; font-size: 21px; color: var(--white); line-height: 1.45;
  }
  .contact ul { list-style: none; margin-top: 10px; }
  .contact li { display: flex; align-items: center; gap: 12px; }
  .contact svg { width: 20px; height: 20px; flex: none; }
  .brand-disc {
    position: absolute; right: 70px; top: 120px;
    width: 320px; height: 320px; border-radius: 50%;
    background: radial-gradient(circle at 65% 35%, var(--amber), var(--orange) 60%, #d85a12);
  }
</style>
</head>
<body>
<main class="stage">
  <section class="card card-back">
    <div class="wordmark">
      <div class="mark-dot"></div>
      <div class="company">HARBINGER<span>CRUDE ADVISORS</span></div>
    </div>
    <p class="tagline">We provide engineering solutions for the complete wellbore cycle from casing design to flowback.</p>
  </section>

  <section class="card card-front">
    <div class="company">HARBINGER<span>CRUDE ADVISORS</span></div>
    <div class="person">
      <p class="name">MARCUS DELANEY</p>
      <p class="role">CEO/FOUNDER</p>
    </div>
    <div class="contact">
      <p>1185 Ridgeline Avenue<br>Fairhaven, WI 53170</p>
      <ul>
        <li><svg viewBox="0 0 20 20"><path d="M5 2l3 4-2 2c1 2.5 3.5 5 6 6l2-2 4 3-2 3C9 18 2 11 2 4z" fill="var(--amber)"/></svg>(262) 555 0147</li>
        <li><svg viewBox="0 0 20 20"><rect x="1.5" y="4.5" width="17" height="11" fill="var(--amber)"/><path d="M1.5 4.5l8.5 6.5 8.5-6.5" fill="none" stroke="#8a4a0a" stroke-width="1.3"/></svg>marcus@harbingercrude.com</li>
        <li><svg viewBox="0 0 20 20"><g fill="none" stroke="var(--amber)" stroke-width="1.6"><circle cx="10" cy="10" r="8"/><ellipse cx="10" cy="10" rx="3.5" ry="8"/><path d="M2 10h16M3.5 6h13M3.5 14h13"/></g></svg>www.harbingercrude.com</li>
      </ul>
    </div>
    <div class="brand-disc"></div>
  </section>
</main>
</body>
</html>
```